Non-Profit needs enticing Winter Advertisement

The Coalition for Clear Pathways (CCPW) is looking to create a dynamic advertising campaign highlighting exciting winter activities in NH. We will also be incorporating drug prevention messaging into these ads.
CCPW is a nonprofit organization that strives to create and promote consistent statewide messages about the problems and solutions of substance misuse in New Hampshire through engagement. We want to highlight the importance of talking to children/teens about the challenges of drug use through the winter.

Our website is here: http://clearpathwaysalliance.org/
Our Facebook page is here:https://www.facebook.com/ClearPathwaysAlliance/

Target Market(s)

Young adults + Parents with kids.

Industry/Entity Type

Government Health Service

Font styles to use
Sans Serif

Colors

Designer to choose colors to be used in the design.

Requirements
Must have
• Please design 1 full-page advertisement with the following idea:
• Image - a family outside skiing/snowboarding, or a mother + son/daughter skiing/snowboarding, or a father + son/daughter skiing/snowboarding
• Text options:
• Start prevention on the bunny hill. Have a conversation with your teen about staying safe this season and all year round.
• Don't let conversations about drugs and alcohol go downhill fast. Take the time to talk with your kids about drugs and alcohol regularly.
• -Something along these lines - a small pun about skiing/winter/cold and then a reminder to start a prevention conversation. If you have a creative idea throw it out there!
• We want to see a colored box at the bottom for more text and logos. Please use the attached photos for inspiration - but again if you think something would look AMAZING you have the freedom to impress us!
Nice to have
• Lato is typically our brand font.
Should not have
• This is not meant to be a scare tactic ad. This is to be a family friendly reminder of bringing the family together/

```html
<!DOCTYPE html>
<html lang="en">
<head>
<meta charset="utf-8">
<title>Winter Prevention Advertisement</title>
<link href="https://fonts.googleapis.com/css2?family=Lato:wght@400;700;900&display=swap" rel="stylesheet">
<style>
  :root {
    --page-bg: #e9e6e1;
    --frame: #8c7f3c;
    --sky-top: #1f6fc4;
    --sky-mid: #8cc3ec;
    --snow: #f3f7fb;
    --navy: #15497d;
    --ink: #1d3f6e;
    --lime: #9fd11c;
    --accent: #f5a11c;
    --white: #ffffff;
  }
  * { box-sizing: border-box; margin: 0; padding: 0; }
  html, body {
    width: 1200px; height: 1000px; overflow: hidden;
    background: var(--page-bg);
    font-family: "Lato", Arial, sans-serif;
  }
  .ad {
    position: absolute; left: 50px; top: 130px;
    width: 1100px; height: 740px;
    border: 4px solid var(--frame);
    overflow: hidden;
    background: var(--snow);
  }
  .hero-photo {
    position: absolute; inset: 0;
    background:
      radial-gradient(ellipse 360px 330px at 820px 330px, #e0437a 0%, #d9353a 35%, rgba(40,110,170,0.85) 70%, rgba(40,110,170,0) 100%),
      linear-gradient(180deg, var(--sky-top) 0%, var(--sky-mid) 45%, var(--snow) 75%, #dfe9f2 100%);
  }
  .brand {
    position: absolute; left: 70px; top: 70px;
    display: flex; align-items: center; gap: 16px;
  }
  .brand-dot {
    width: 34px; height: 34px; border-radius: 50%;
    background: var(--accent);
  }
  .brand-name {
    font-weight: 900; font-size: 38px; line-height: 1.05;
    color: var(--ink); width: 380px;
  }
  .message-panel {
    position: absolute; left: 100px; top: 250px;
    width: 380px; height: 310px;
    background: rgba(255,255,255,0.72);
    box-shadow: 0 0 40px 30px rgba(255,255,255,0.72);
    border-radius: 20px;
  }
  .message-list {
    position: absolute; left: 110px; top: 265px; width: 390px;
    list-style: none;
  }
  .message-list li {
    position: relative; padding-left: 34px;
    font-weight: 700; font-size: 22px; line-height: 1.3;
    color: var(--ink); margin-bottom: 26px;
  }
  .tick {
    position: absolute; left: 0; top: 4px; width: 22px; height: 22px;
  }
  .info-band {
    position: absolute; left: 520px; top: 585px; right: 0; bottom: 0;
    background: var(--navy);
  }
  .base-strip {
    position: absolute; left: 0; right: 0; bottom: 0; height: 30px;
    background: var(--navy);
  }
  .text-box {
    position: absolute; left: 160px; top: 545px;
    width: 540px; height: 165px;
    background: var(--lime);
    clip-path: polygon(0 0, 100% 0, 90% 100%, 0 100%);
  }
  .web-address {
    position: absolute; left: 700px; top: 665px;
    font-size: 22px; font-weight: 400; color: var(--white);
  }
  .social-handle {
    position: absolute; right: 40px; top: 600px;
    display: flex; align-items: center; gap: 10px;
    font-size: 22px; font-weight: 400; color: var(--white);
  }
  .social-square {
    width: 20px; height: 20px; background: var(--white);
  }
</style>
</head>
<body>
  <section class="ad">
    <div class="hero-photo" role="img" aria-label="Photograph of a smiling family in ski helmets and goggles on a snowy mountain slope under a blue sky, skis standing in the snow"></div>

    <div class="brand">
      <span class="brand-dot"></span>
      <span class="brand-name">The Coalition for Clear Pathways</span>
    </div>

    <div class="message-panel"></div>
    <ul class="message-list">
      <li>
        <svg class="tick" viewBox="0 0 22 22"><circle cx="11" cy="11" r="9.5" fill="none" stroke="#1d3f6e" stroke-width="2"/><path d="M6.5 11.5l3 3 6-7" fill="none" stroke="#1d3f6e" stroke-width="2.4" stroke-linecap="round" stroke-linejoin="round"/></svg>
        Start prevention on the bunny hill. Have a conversation with your teen about staying safe this season and all year round.
      </li>
      <li>
        <svg class="tick" viewBox="0 0 22 22"><circle cx="11" cy="11" r="9.5" fill="none" stroke="#1d3f6e" stroke-width="2"/><path d="M6.5 11.5l3 3 6-7" fill="none" stroke="#1d3f6e" stroke-width="2.4" stroke-linecap="round" stroke-linejoin="round"/></svg>
        Don't let conversations about drugs and alcohol go downhill fast. Take the time to talk with your kids about drugs and alcohol regularly.
      </li>
    </ul>

    <div class="info-band"></div>
    <div class="base-strip"></div>
    <div class="text-box"></div>

    <p class="web-address">www.clearpathwaysalliance.org</p>
    <p class="social-handle"><span class="social-square"></span>ClearPathwaysAlliance</p>
  </section>
</body>
</html>
```